Professional IT Company Letterhead

We need a new letterhead design to incorporate our new login and business card design recently received here on Sketch Guild. We want the same look and feel as the other two accepted projects. We want a professional and clean design.

Target Market(s)

Medical/Dental and Professional Services Businesses (CPA, Attorney, Architect etc)

Industry/Entity Type

Business

Requirements
Must have
• Clean and professional, consistent brand with our current design of our new logo and business cards.
Nice to have
• Would like to also be able to use the design on our newsletter header

```html
<!DOCTYPE html>
<html lang="en">
<head>
<meta charset="UTF-8">
<title>Tidewell Technology Letterhead</title>
<link rel="stylesheet" href="https://fonts.googleapis.com/css2?family=Jost:wght@400;500&family=Quicksand:wght@500&display=swap">
<style>
  :root {
    --backdrop: #cbcbcb;
    --paper-top: #ffffff;
    --paper-mid: #eaf2f9;
    --paper-bottom: #c2daef;
    --brand-blue: #1b9ad6;
    --brand-deep: #1a6fb5;
    --ink: #23344a;
    --water-light: #7fb7e3;
    --water-deep: #2a7dc6;
  }
  * { margin: 0; padding: 0; box-sizing: border-box; }
  html, body {
    width: 1200px; height: 1200px; overflow: hidden;
    background: var(--backdrop);
  }
  .letterhead {
    position: absolute;
    left: 277px; top: 143px;
    width: 646px; height: 914px;
    background: linear-gradient(to bottom,
      var(--paper-top) 0%, var(--paper-top) 17%,
      var(--paper-mid) 45%, var(--paper-bottom) 100%);
  }
  .brand {
    position: absolute; left: 62px; top: 52px;
    display: flex; flex-direction: column; align-items: flex-start;
  }
  .brand-row { display: flex; align-items: center; gap: 10px; }
  .brand-mark {
    width: 34px; height: 34px; border-radius: 50%;
    background: var(--brand-blue);
  }
  .brand-name {
    font-family: "Quicksand", sans-serif;
    font-weight: 500; font-size: 30px; line-height: 1;
    color: var(--brand-blue);
    letter-spacing: -0.3px;
  }
  .brand-tagline {
    margin-top: 8px;
    font-family: "Quicksand", sans-serif;
    font-weight: 500; font-size: 8.5px; letter-spacing: 0.9px;
    color: var(--brand-blue);
  }
  .waterline {
    position: absolute; left: 0; top: 826px;
    width: 100%; height: 20px; display: block;
  }
  .contact {
    position: absolute; left: 0; right: 0; top: 862px;
    text-align: center;
    font-family: "Jost", sans-serif; font-size: 11px; line-height: 14px;
    color: var(--ink);
  }
  .contact-row { display: flex; justify-content: center; align-items: center; gap: 5px; }
  .contact-icon { width: 9px; height: 9px; fill: var(--brand-deep); }
</style>
</head>
<body>
  <main class="letterhead">
    <header class="brand">
      <div class="brand-row">
        <span class="brand-mark"></span>
        <span class="brand-name">Tidewell Technology</span>
      </div>
      <p class="brand-tagline">IT Support for Medical &amp; Dental Practices</p>
    </header>

    <svg class="waterline" viewBox="0 0 646 20" preserveAspectRatio="none" role="img" aria-label="Band of rippling water surface">
      <defs>
        <linearGradient id="water-band" x1="0" y1="0" x2="0" y2="1">
          <stop offset="0" stop-color="var(--water-deep)" stop-opacity="0.9"/>
          <stop offset="0.5" stop-color="var(--water-light)" stop-opacity="0.5"/>
          <stop offset="1" stop-color="var(--water-light)" stop-opacity="0"/>
        </linearGradient>
      </defs>
      <rect x="0" y="2" width="646" height="18" fill="url(#water-band)"/>
    </svg>

    <footer class="contact">
      <div class="contact-row">
        <svg class="contact-icon" viewBox="0 0 10 10"><path d="M1 3c0-1 1-2 4-2s4 1 4 2v1H7V3H3v1H1zM2 5h6l1 4H1z"/></svg>
        <span>+00 111 222 3333</span>
        <svg class="contact-icon" viewBox="0 0 10 10"><path d="M0 2h10v6H0zM1 3l4 3 4-3" stroke="#fff" stroke-width="0.8"/></svg>
        <span>yourname@yourwebsite.com</span>
        <svg class="contact-icon" viewBox="0 0 10 10"><circle cx="5" cy="5" r="4.5"/><path d="M0.5 5h9M5 0.5v9" stroke="#fff" stroke-width="0.7"/></svg>
        <span>www.yourwebsite.com</span>
      </div>
      <div>Your Long Commercial or business address in 2 line</div>
    </footer>
  </main>
</body>
</html>
```